Social Media Graphics - Copperfield Loop

Create 6-7 individual social media graphics (square size) to encourage folks to join our online course, using either of the text below (only one set of text per graphic:

The Lantern Ridge Method
How to Create a 7-Figure Business From Scratch
Sign Up Today!

Or

The Lantern Ridge Method
Fast-track Your Way to a Multi-Million Business!
Sign Up Today!

For the color scheme of the graphics, use 1 or 2 colors in the color palette attached; or use any colors that look nice with their outfits; AVOID using red, white and blue altogether because it will look like an Independence Day (4th of July) graphic and we don’t want that; make sure the graphics appeal to both men and women

Make sure each graphic contains 1 of the 2 pics attached; and make sure one of the graphics is all TEXT only.

Target Market(s)

men and women looking to make more money

Industry/Entity Type

entrepreneurship

Requirements
Must have
• see the text document attached
Nice to have
• We are open to a nice color design; the color palette colors are not required, especially we don't want red, white and blue used together
Should not have
• AVOID using red, white and blue altogether because it will look like an Independence Day (4th of July) graphic and we dont want that

```html
<!DOCTYPE html>
<html lang="en">
<head>
<meta charset="utf-8">
<title>The Lantern Ridge Method — Social Graphics</title>
<link href="https://fonts.googleapis.com/css2?family=Montserrat:wght@500;700&display=swap" rel="stylesheet">
<style>
:root{
  --red:#ee2c42;
  --crimson:#ce1128;
  --plum:#3a1252;
  --blush:#fbd6d6;
  --rose:#f8b9c2;
  --white:#ffffff;
  --ink:#3b3036;
}
*{box-sizing:border-box;margin:0;padding:0}
html,body{width:1200px;height:802px;overflow:hidden;background:var(--white)}
body{position:relative;font-family:"Montserrat",sans-serif}
.tile{position:absolute;width:387px;height:386px;overflow:hidden}
.tile--red{background:var(--red)}
.tile--crimson{background:var(--crimson)}
.tile--plum{background:var(--plum)}
.accent-bar{position:absolute;width:4px;background:var(--blush)}
.copy{position:absolute;color:var(--white);white-space:nowrap}
.copy__title{font-weight:700;font-size:20.5px;letter-spacing:-.3px;line-height:26px}
.copy__lead{font-weight:500;font-size:19px;line-height:26px;margin-top:19px}
.badge{position:absolute}
.badge svg{position:absolute;inset:0;width:100%;height:100%}
.badge__text{position:absolute;inset:0;display:flex;align-items:center;justify-content:center;text-align:center;font-weight:500;line-height:1.2;transform:rotate(-14deg)}
.arrow{position:absolute}
.dollar{position:absolute;color:var(--blush);font-weight:700;line-height:1}
.photo{position:absolute}
.icon{position:absolute}
</style>
</head>
<body>

<section class="tile tile--red" style="left:10px;top:10px">
  <div class="accent-bar" style="left:28px;top:0;height:190px"></div>
  <div class="copy" style="left:60px;top:79px">
    <h2 class="copy__title">The Lantern Ridge Method</h2>
    <p class="copy__lead">Fast-track Your Way<br>to a Multi-Million<br>Business!</p>
  </div>
  <div class="badge" style="left:196px;top:203px;width:166px;height:166px">
    <svg viewBox="0 0 100 100"><circle cx="50" cy="50" r="44" fill="#f8b9c2"/><circle cx="50" cy="50" r="45" fill="none" stroke="#f8b9c2" stroke-width="9" stroke-linecap="round" stroke-dasharray="0 10.1"/></svg>
    <div class="badge__text" style="color:var(--ink);font-size:23px">Sign Up<br>Today!</div>
  </div>
  <svg class="arrow" style="left:32px;top:260px" width="78" height="126" viewBox="0 0 78 126"><polygon points="0,40 39,0 78,40 58,40 58,126 20,126 20,40" fill="#fbd6d6"/></svg>
  <svg class="arrow" style="left:92px;top:312px" width="78" height="74" viewBox="0 0 78 74"><polygon points="0,38 39,0 78,38 58,38 58,74 20,74 20,38" fill="#ffffff"/></svg>
</section>

<section class="tile tile--crimson" style="left:406px;top:10px">
  <svg class="photo" style="left:140px;top:0" width="247" height="222" viewBox="0 0 247 222">
    <defs><linearGradient id="g2" x1="0" x2="1"><stop offset="0" stop-color="#e9748a"/><stop offset=".5" stop-color="#c23a5c"/><stop offset="1" stop-color="#2a2326"/></linearGradient></defs>
    <polygon points="20,0 247,0 247,190 40,215" fill="#ffffff"/>
    <polygon points="60,0 247,0 247,180" fill="#f8d3d8"/>
    <polygon role="img" aria-label="Photo of the two course hosts standing with arms crossed" points="40,30 120,0 240,0 240,190 60,210" fill="url(#g2)"/>
  </svg>
  <span class="dollar" style="left:22px;top:14px;font-size:40px">$</span>
  <span class="dollar" style="left:36px;top:176px;font-size:28px">$</span>
  <span class="dollar" style="left:154px;top:172px;font-size:40px">$</span>
  <div class="badge" style="left:42px;top:34px;width:138px;height:138px">
    <svg viewBox="0 0 100 100"><circle cx="50" cy="50" r="44" fill="#fbd6d6"/><circle cx="50" cy="50" r="45" fill="none" stroke="#fbd6d6" stroke-width="9" stroke-linecap="round" stroke-dasharray="0 10.1"/></svg>
    <div class="badge__text" style="color:var(--crimson);font-size:19px">Sign Up<br>Today!</div>
  </div>
  <div class="accent-bar" style="left:32px;top:238px;height:148px"></div>
  <div class="copy" style="left:58px;top:235px">
    <h2 class="copy__title">The Lantern Ridge Method</h2>
    <p class="copy__lead">How to Create a<br>7-Figure Business<br>From Scratch</p>
  </div>
  <svg class="arrow" style="left:304px;top:312px" width="68" height="74" viewBox="0 0 68 74"><polygon points="0,34 34,0 68,34 50,34 50,74 18,74 18,34" fill="#ffffff"/></svg>
</section>

<section class="tile tile--plum" style="left:803px;top:10px">
  <div class="accent-bar" style="left:30px;top:0;height:190px"></div>
  <div class="copy" style="left:61px;top:79px">
    <h2 class="copy__title">The Lantern Ridge Method</h2>
    <p class="copy__lead">How to Create a<br>7-Figure Business<br>From Scratch</p>
  </div>
  <div class="badge" style="left:197px;top:203px;width:166px;height:166px">
    <svg viewBox="0 0 100 100"><circle cx="50" cy="50" r="44" fill="#ee2c42"/><circle cx="50" cy="50" r="45" fill="none" stroke="#ee2c42" stroke-width="9" stroke-linecap="round" stroke-dasharray="0 10.1"/></svg>
    <div class="badge__text" style="color:var(--blush);font-size:23px">Sign Up<br>Today!</div>
  </div>
  <svg class="arrow" style="left:33px;top:260px" width="78" height="126" viewBox="0 0 78 126"><polygon points="0,40 39,0 78,40 58,40 58,126 20,126 20,40" fill="#fbd6d6"/></svg>
  <svg class="arrow" style="left:93px;top:312px" width="78" height="74" viewBox="0 0 78 74"><polygon points="0,38 39,0 78,38 58,38 58,74 20,74 20,38" fill="#f8b9c2"/></svg>
</section>

<section class="tile tile--red" style="left:10px;top:406px">
  <div class="accent-bar" style="left:28px;top:0;height:148px"></div>
  <div class="copy" style="left:57px;top:33px">
    <h2 class="copy__title">The Lantern Ridge Method</h2>
    <p class="copy__lead">How to Create a<br>7-Figure Business<br>From Scratch</p>
  </div>
  <svg class="photo" style="left:-10px;top:172px" width="250" height="240" viewBox="0 0 250 240">
    <defs><linearGradient id="g4" x1="0" x2="1"><stop offset="0" stop-color="#f3c5c9"/><stop offset=".5" stop-color="#d9567a"/><stop offset="1" stop-color="#2f282b"/></linearGradient></defs>
    <circle role="img" aria-label="Photo of the two course hosts in a circle frame" cx="125" cy="125" r="122" fill="url(#g4)"/>
  </svg>
  <div class="badge" style="left:204px;top:145px;width:126px;height:126px">
    <svg viewBox="0 0 100 100"><circle cx="50" cy="50" r="44" fill="#fbd6d6"/><circle cx="50" cy="50" r="45" fill="none" stroke="#fbd6d6" stroke-width="9" stroke-linecap="round" stroke-dasharray="0 10.1"/></svg>
    <div class="badge__text" style="color:var(--ink);font-size:18px">Sign Up<br>Today!</div>
  </div>
  <svg class="icon" style="left:270px;top:284px" width="84" height="88" viewBox="0 0 84 88">
    <rect x="2" y="60" width="18" height="28" fill="#fbd6d6"/>
    <rect x="30" y="46" width="18" height="42" fill="#fbd6d6"/>
    <rect x="58" y="30" width="18" height="58" fill="#fbd6d6"/>
    <polyline points="2,44 30,26 44,32 74,8" fill="none" stroke="#fbd6d6" stroke-width="6" stroke-linejoin="round"/>
    <polygon points="62,2 82,0 78,20" fill="#fbd6d6"/>
  </svg>
</section>

<section class="tile tile--plum" style="left:406px;top:406px">
  <div class="accent-bar" style="left:32px;top:0;height:150px"></div>
  <div class="copy" style="left:58px;top:33px">
    <h2 class="copy__title">The Lantern Ridge Method</h2>
    <p class="copy__lead">Fast-track Your Way<br>to a Multi-Million<br>Business!</p>
  </div>
  <svg class="photo" style="left:-2px;top:174px" width="240" height="240" viewBox="0 0 240 240">
    <defs><linearGradient id="g5" x1="0" x2="1"><stop offset="0" stop-color="#c0705a"/><stop offset=".5" stop-color="#2b2628"/><stop offset="1" stop-color="#6b4a5e"/></linearGradient></defs>
    <circle role="img" aria-label="Photo of the two course hosts in a circle frame" cx="120" cy="120" r="119" fill="url(#g5)"/>
  </svg>
  <div class="badge" style="left:234px;top:138px;width:126px;height:126px">
    <svg viewBox="0 0 100 100"><circle cx="50" cy="50" r="44" fill="#fbd6d6"/><circle cx="50" cy="50" r="45" fill="none" stroke="#fbd6d6" stroke-width="9" stroke-linecap="round" stroke-dasharray="0 10.1"/></svg>
    <div class="badge__text" style="color:var(--plum);font-size:18px">Sign Up<br>Today!</div>
  </div>
  <svg class="icon" style="left:276px;top:280px" width="68" height="94" viewBox="0 0 68 94" fill="none" stroke="#fbd6d6" stroke-width="4" stroke-linejoin="round">
    <path d="M22 4 L46 4 L40 20 L28 20 Z"/>
    <path d="M26 22 L42 22"/>
    <path d="M28 26 C8 38 2 60 4 74 C6 88 20 91 34 91 C48 91 62 88 64 74 C66 60 60 38 40 26 Z"/>
    <text x="34" y="76" text-anchor="middle" fill="#fbd6d6" stroke="none" font-family="Montserrat, sans-serif" font-weight="700" font-size="30">$</text>
  </svg>
</section>

<section class="tile tile--plum" style="left:803px;top:406px">
  <svg class="photo" style="left:140px;top:0" width="247" height="222" viewBox="0 0 247 222">
    <defs><linearGradient id="g6" x1="0" x2="1"><stop offset="0" stop-color="#2b2628"/><stop offset=".5" stop-color="#c0705a"/><stop offset="1" stop-color="#6b4a5e"/></linearGradient></defs>
    <polygon points="20,0 247,0 247,200 70,215" fill="#fbd6d6"/>
    <rect role="img" aria-label="Photo of the two course hosts standing with arms crossed" x="32" y="0" width="215" height="200" fill="url(#g6)"/>
  </svg>
  <span class="dollar" style="left:22px;top:12px;font-size:40px">$</span>
  <span class="dollar" style="left:36px;top:176px;font-size:28px">$</span>
  <span class="dollar" style="left:154px;top:172px;font-size:40px">$</span>
  <div class="badge" style="left:44px;top:36px;width:138px;height:138px">
    <svg viewBox="0 0 100 100"><circle cx="50" cy="50" r="44" fill="#fbd6d6"/><circle cx="50" cy="50" r="45" fill="none" stroke="#fbd6d6" stroke-width="9" stroke-linecap="round" stroke-dasharray="0 10.1"/></svg>
    <div class="badge__text" style="color:var(--plum);font-size:19px">Sign Up<br>Today!</div>
  </div>
  <div class="accent-bar" style="left:33px;top:238px;height:148px"></div>
  <div class="copy" style="left:57px;top:234px">
    <h2 class="copy__title">The Lantern Ridge Method</h2>
    <p class="copy__lead">Fast-track Your Way<br>to a Multi-Million<br>Business!</p>
  </div>
  <svg class="arrow" style="left:294px;top:292px" width="78" height="94" viewBox="0 0 78 94"><polygon points="0,38 39,0 78,38 58,38 58,94 20,94 20,38" fill="#fbd6d6"/></svg>
</section>

</body>
</html>
```